Logo and Flyer for Co-Branded Comedy Show

Graphic designer needed to create a promotional flyer for a comedy show. Two different comedy shows, with distinct branding, are joining forces to create a combined show. (co-branded logo to be included is attached.)

The design of the promotional materials should be a modern take on a vintage poster a la Quirkwood Jamboree. We'd like it to be a vintage look with a modern twist (I have attached the Quirkwood Jamboree Flyer for reference - marked up with info for our show) Filename: PLGRVN Flyer Mark Up

Images of the two hosts are attached: Filenames:

Our show will be in a theater, so if it can play off a playbill that would be great. I have attached examples of the clean look that we like, as well as some vintage theater flyers. We'd like to stay on the lighter side of the color palette (light gray, blues, etc. which is in line with the Harbor Laughs Live flyer) Filename: PLGR VN Flyer Direction

Current Branding of the individual Shows
I have attached the current promo materials for the individual shows, so you have a sense of the color palette and logo treatment.

The deliverable:
1 flyer vertical, 1 flyer horizontal - same design/concept but in 2 orientation (vertical and horizontal) horizontal will be used for web.
***This flyer will include the co-branded logo seen attached - Harbor Laughs Live Gets Real Honest (individual logos already created and attached) - Download PSD File here: http://lnk.example-short.test/PLGRVN

Industry/Entity Type

Graphic Designer

Colors
0493cd
85cae6
ecf7fb
f5f5f5
ffffff
606060
fbfbfb
0255a3
3176b5

Requirements
Must have
• Vintage look with a modern twist
• Vertical and horizontal options

```html
<!DOCTYPE html>
<html lang="en">
<head>
<meta charset="utf-8">
<title>Harbor Laughs Live – Comedy Show Flyer</title>
<link rel="stylesheet" href="https://fonts.googleapis.com/css2?family=Bebas+Neue&family=Poiret+One&display=swap">
<style>
  :root {
    --backdrop: #c4b59a;
    --paper: #ebebed;
    --paper-shade: #e1e1e6;
    --paper-edge: #b9b8dc;
    --brand-blue: #3a5fb0;
    --band-blue: #3358a8;
    --ink: #1a1a1a;
    --white: #ffffff;
    --photo-warm: #b58a6c;
    --photo-cool: #4a5a4a;
  }
  * { margin: 0; padding: 0; box-sizing: border-box; }
  html, body { width: 1146px; height: 1200px; overflow: hidden; background: var(--backdrop); }
  .flyer {
    position: absolute; left: 203px; top: 51px; width: 705px; height: 1089px;
    background:
      linear-gradient(to bottom, var(--paper-edge) 0, rgba(185,184,220,0) 34px),
      linear-gradient(to top, var(--paper-edge) 0, rgba(185,184,220,0) 46px),
      radial-gradient(ellipse at 50% 45%, var(--paper) 55%, var(--paper-shade) 100%);
    font-family: "Bebas Neue", "Oswald", sans-serif;
    color: var(--brand-blue);
  }
  .centered { position: absolute; left: 0; width: 100%; text-align: center; }
  .presenter { top: 55px; font-size: 29px; letter-spacing: 1px; }
  .thin { font-family: "Poiret One", "Didact Gothic", sans-serif; color: var(--ink); }
  .presents { top: 88px; font-size: 24px; }
  .rule { position: absolute; height: 1px; background: var(--brand-blue); }
  .ornament { position: absolute; top: 228px; width: 110px; height: 62px; background: var(--ink); }
  .ornament-left { left: 38px; }
  .ornament-right { left: 557px; }
  .show-title { position: absolute; left: 156px; width: 393px; top: 186px; text-align: center; font-size: 62px; line-height: 62px; letter-spacing: 1px; font-weight: 400; }
  .show-title-sub { display: block; font-size: 40px; line-height: 46px; letter-spacing: 6px; }
  .comedy-show { top: 353px; font-size: 30px; }
  .date { top: 397px; font-size: 35px; letter-spacing: 1px; }
  .host-photo {
    position: absolute; top: 517px; width: 196px; height: 196px; border-radius: 50%;
    border: 3px solid var(--white);
  }
  .host-photo-left { left: 67px; background: radial-gradient(circle at 50% 40%, var(--photo-warm) 0 38%, #222 70%); }
  .host-photo-right { left: 436px; background: radial-gradient(circle at 50% 40%, #6b4632 0 35%, var(--photo-cool) 72%); }
  .hosted-by { position: absolute; left: 292px; width: 120px; top: 572px; font-size: 30px; line-height: 46px; text-align: center; }
  .host-name { position: absolute; top: 740px; width: 300px; text-align: center; font-size: 30px; letter-spacing: 1px; }
  .host-name-left { left: 15px; }
  .host-name-right { left: 384px; }
  .featuring { top: 810px; font-size: 19px; color: var(--brand-blue); }
  .lineup { top: 840px; font-size: 34px; line-height: 44px; color: var(--ink); letter-spacing: 1px; }
  .venue-band {
    position: absolute; left: 0; top: 934px; width: 100%; height: 42px;
    background: var(--band-blue); color: var(--white);
    font-size: 23px; letter-spacing: 3px; line-height: 44px; text-align: center;
  }
  .website { top: 1008px; font-size: 25px; letter-spacing: 5px; }
</style>
</head>
<body>
  <main class="flyer">
    <p class="centered presenter">Pale Birch Productions</p>
    <span class="rule" style="left:186px; top:105px; width:100px;"></span>
    <p class="centered thin presents">presents</p>
    <span class="rule" style="left:412px; top:105px; width:101px;"></span>

    <div class="ornament ornament-left" role="img" aria-label="Black ribbon banner ornament with star"></div>
    <h1 class="show-title">Harbor Laughs<span class="show-title-sub">Live</span></h1>
    <div class="ornament ornament-right" role="img" aria-label="Black ribbon banner ornament with star"></div>

    <p class="centered thin comedy-show">comedy show</p>
    <span class="rule" style="left:133px; top:391px; width:437px;"></span>
    <p class="centered date">Saturday Night 22nd August, 2015</p>

    <div class="host-photo host-photo-left" role="img" aria-label="Portrait photo of host Zolo Brightwave"></div>
    <p class="thin hosted-by">hosted<br>by</p>
    <div class="host-photo host-photo-right" role="img" aria-label="Portrait photo of host Marla Vintrow"></div>

    <p class="host-name host-name-left">Zolo Brightwave</p>
    <p class="host-name host-name-right">Marla Vintrow</p>

    <p class="centered thin featuring">featuring</p>
    <p class="centered lineup">Toby Lancer Heston Grayvale Norrin Mackleby<br>Lisa Torven Gideon Marsh Norvale &amp; More</p>

    <div class="venue-band">Lantern Hall Theatre, 214 Ferris Ave, Harborview, NY 10990</div>

    <p class="centered website">PLGRVN.COM</p>
  </main>
</body>
</html>
```